Business Cards for Law Office of Denise R. Harlow

I need a business card for my new estate planning law firm. I have attached my logo. I would like a design that is professional but not too formal or stuffy.

Target Market(s)

Professionals (lawyers, doctors, businesswomen) between the age of 30 and 50 who are tech-savvy and educated.

Industry/Entity Type

Lawyer

Contact Information for Business Card

Denise R. Harlow

528 E. 19th Street
7th Floor
New York, NY 10583

Phone: (855) 602-7318
Direct: (917) 463-5071
Email: Denise@DeniseRHarlowLegal.test
www.DeniseRHarlowLegal.test

Font styles to use
Other font styles liked:
• Corbel

Requirements
Must have
• On the front:
• Denise R. Harlow, Esq.
• Owner & Founder
• 528 E. 19th Street
• 7th Floor
• New York, NY 10583
• Phone: (855) 602-7318
• Direct: (917) 463-5071
• Email: denise@deniserharlowlegal.test
• www.deniserharlowlegal.test
• On the back:
• LOGO
Nice to have
• I want it to be professional but not too formal or stuffy. Please choose colors that go with my logo.
Should not have
• I don't want TOO MUCH color. Some color is good, but not too much.

```html
<!DOCTYPE html>
<html lang="en">
<head>
<meta charset="utf-8">
<title>Denise R. Harlow – Business Card</title>
<link href="https://fonts.googleapis.com/css2?family=Alegreya+Sans:wght@400;500&family=Encode+Sans+Condensed:wght@400&display=swap" rel="stylesheet">
<style>
  :root {
    --page: #ffffff;
    --panel: #fcfcfc;
    --ink: #111111;
    --purple: #7d2a7e;
    --purple-soft: #8e3e9b;
    --orange: #f29a35;
    --band: #b3b1b3;
    --white: #ffffff;
  }
  html, body {
    margin: 0;
    padding: 0;
    width: 921px;
    height: 1200px;
    overflow: hidden;
    background: var(--page);
  }
  .canvas {
    position: relative;
    width: 921px;
    height: 1200px;
    overflow: hidden;
    font-family: "Alegreya Sans", sans-serif;
    color: var(--ink);
  }
  .card-back {
    position: absolute;
    left: 33px;
    top: 29px;
    width: 860px;
    height: 491px;
    background: var(--panel);
  }
  .logo-area {
    position: absolute;
    left: 45px;
    top: 135px;
    width: 765px;
    height: 223px;
    background: var(--white);
    display: flex;
    align-items: center;
    justify-content: center;
  }
  .firm-name {
    font-family: "Alegreya Sans", sans-serif;
    font-weight: 500;
    font-size: 50px;
    color: var(--purple);
    margin: 0;
    letter-spacing: 0.5px;
  }
  .card-front {
    position: absolute;
    left: 33px;
    top: 647px;
    width: 860px;
    height: 274px;
    background: var(--panel);
  }
  .holder {
    position: absolute;
    left: 0;
    right: 0;
    top: 100px;
    text-align: center;
    font-family: "Encode Sans Condensed", sans-serif;
  }
  .holder-name {
    margin: 0;
    font-size: 52px;
    font-weight: 400;
    line-height: 60px;
    color: var(--ink);
  }
  .holder-title {
    margin: 0;
    font-size: 40px;
    font-weight: 400;
    line-height: 52px;
    color: var(--purple-soft);
  }
  .contact-band {
    position: absolute;
    left: 0;
    top: 921px;
    width: 921px;
    height: 279px;
    background: var(--band);
  }
  .contact-rails {
    position: absolute;
    left: 0;
    top: 921px;
  }
  .contact-line {
    position: absolute;
    margin: 0;
    font-size: 24px;
    line-height: 28px;
    color: var(--ink);
    white-space: nowrap;
  }
  .contact-phone   { left: 168px; top: 942px; }
  .contact-email   { left: 143px; top: 997px; }
  .contact-web     { left: 121px; top: 1055px; }
  .contact-address { left: 102px; top: 1114px; }
</style>
</head>
<body>
<div class="canvas">

  <section class="card-back">
    <div class="logo-area">
      <p class="firm-name">Law Office of Denise R. Harlow</p>
    </div>
  </section>

  <section class="card-front">
    <div class="holder">
      <h1 class="holder-name">Denise R. Harlow</h1>
      <p class="holder-title">Owner &amp; Founder</p>
    </div>
  </section>

  <div class="contact-band"></div>

  <svg class="contact-rails" width="921" height="279" viewBox="0 921 921 279" aria-hidden="true">
    <!-- rails -->
    <rect x="60" y="921" width="18" height="209" fill="var(--orange)"/>
    <rect x="82" y="921" width="16" height="147" fill="var(--white)"/>
    <rect x="105" y="921" width="16" height="90" fill="var(--orange)"/>
    <rect x="127" y="921" width="16" height="33" fill="var(--white)"/>

    <!-- phone -->
    <circle cx="133" cy="954" r="23" fill="var(--white)"/>
    <path d="M124 942 l5 -2 l4 8 l-3 3 q2 6 7 10 l3 -3 l8 4 l-2 5 q-3 2 -7 1 q-12 -6 -17 -19 q-1 -4 2 -7 z" fill="var(--ink)"/>

    <!-- email -->
    <circle cx="111" cy="1011" r="23" fill="var(--orange)"/>
    <text x="111" y="1020" text-anchor="middle" font-family="Alegreya Sans, sans-serif" font-size="28" font-weight="500" fill="var(--white)">@</text>

    <!-- web -->
    <circle cx="88" cy="1068" r="23" fill="var(--white)"/>
    <circle cx="88" cy="1068" r="14" fill="none" stroke="var(--ink)" stroke-width="3"/>
    <path d="M80 1060 q6 2 5 8 q-4 3 -2 9 M94 1058 q-4 5 2 9 q3 2 4 6" fill="none" stroke="var(--ink)" stroke-width="3"/>

    <!-- address -->
    <circle cx="67" cy="1130" r="23" fill="var(--orange)"/>
    <path d="M67 1144 q-10 -12 -10 -19 a10 10 0 0 1 20 0 q0 7 -10 19 z" fill="var(--white)"/>
    <circle cx="67" cy="1125" r="3.5" fill="var(--orange)"/>
  </svg>

  <p class="contact-line contact-phone">Phone: (855) 602-7318 - Direct: (917) 463-5071</p>
  <p class="contact-line contact-email">denise@deniserharlowlegal.test</p>
  <p class="contact-line contact-web">www.deniserharlowlegal.test</p>
  <p class="contact-line contact-address">528 E. 19th Street-7th Floor-New York, NY 10583</p>

</div>
</body>
</html>
```